Vantry Forge (IT/Network Services)

Vantry Forge, LLC provides technology services to small and medium businesses. Essentially, anytime you've every thought your business might need an "IT guy" to handle something you could instead call us to handle it. Basically, you can outsource your IT needs to us.

This is a brand new company and so we'll need a brand new website. I'd like to use WordPress to handle the site since that will make things easier for me to maintain in the long run.

The site should include a, more-or-less, static front page with the dynamic data occurring on pages linked from a navigational area.

I have a logo already designed that I would like to see used in the design. The one with "white" in the title is the official logo, just added some other versions for your perusal.

Color queues from the logo but feel free to add other colors where applicable.

The site should feel somewhat corporate but with a "younger" slant (something a 25-35 year old would enjoy).

Pages (either to be added initially or by me after design completion):
"About" section - includes company history, business philosophy, etc.
"Services" section - service options, service approach, service specifics
"Testimonials" section - (eventually)
"News" section - (eventually) industry news, company news, events, blog
Contact Links

Websites to view:
The two largest local competitors:
http://www.harbelmsystemsinc.example/
http://www.qubrix.example/
Other local competitors:
http://www.plkllc.example/
http://www.merowaygroup.example/

Other info you might find useful:
Domain: vfllc.example
Address:
517 Calder Ln W
Suite 742B
Nashville, TN 37288
Phone: 615-555-0187
Emails available for use/display:
info@vfllc.example
sales@vfllc.example

Target Market(s)

Our target clients are mainly small businesses (25 or less computer users) which means we're looking at a lot of start-ups or younger companies. We'll be interacting with many entrepreneurs and young business owners.

Requirements
Must have
• Need full WP theme (not a mockup)

```html
<!DOCTYPE html>
<html lang="en">
<head>
<meta charset="utf-8">
<title>Vantry Forge — IT &amp; Network Services</title>
<link rel="stylesheet" href="https://fonts.googleapis.com/css2?family=Days+One&family=Montserrat:wght@400;500;600;700&family=Open+Sans:ital,wght@0,400;0,600;0,700;1,400;1,700&display=swap">
<style>
:root{
  --ink-dark:#2b2b2b;
  --ink-darker:#232323;
  --orange:#f39417;
  --orange-deep:#e57d0a;
  --navy:#2a3644;
  --navy-footer:#243039;
  --slate:#3d4a57;
  --muted:#7f93a8;
  --panel:#f4f4f4;
  --hero-blue:#175d98;
  --white:#ffffff;
}
*{margin:0;padding:0;box-sizing:border-box}
html,body{width:931px;height:1200px;overflow:hidden}
body{position:relative;background:#fff;font-family:"Open Sans",Arial,sans-serif;color:var(--slate)}
.top-band{position:absolute;left:0;top:0;width:931px;height:366px;background:linear-gradient(90deg,var(--ink-darker),#333 50%,var(--ink-darker))}
.fade-band{position:absolute;left:0;top:366px;width:931px;height:240px;background:linear-gradient(#e4e5e7,#fff)}
.brand{position:absolute;left:116px;top:20px;display:flex;align-items:center;gap:10px}
.brand-dot{width:30px;height:30px;border-radius:50%;background:var(--orange)}
.brand-name{font-family:"Montserrat",sans-serif;font-weight:700;font-size:27px;color:#8c8c8c;letter-spacing:.5px}
.header-contact{position:absolute;right:118px;top:22px;text-align:right}
.header-contact .phone{font-size:17px;font-weight:600;color:#f2f2f2;line-height:20px}
.header-contact .email{font-size:14px;color:#a8a8a8;line-height:18px}
.main-nav{position:absolute;left:116px;top:81px;width:697px;height:33px;display:flex;border-radius:4px 4px 0 0;background:linear-gradient(#fbb02f,var(--orange) 55%,var(--orange-deep));overflow:hidden}
.main-nav a{display:flex;align-items:center;justify-content:center;color:#fff;text-decoration:none;font-size:13px;font-weight:600;border-right:1px solid #d7760a;box-shadow:inset -1px 0 0 #fcb74a}
.main-nav a:last-child{border:0;box-shadow:none}
.hero{position:absolute;left:116px;top:114px;width:697px;height:300px;background:linear-gradient(100deg,#f4f6f9 0%,#dfe6ee 30%,#c9d3df 45%,#e9d3bf 62%,#f0dcc8 78%,#d7c2ae 100%);overflow:hidden}
.hero-title{position:absolute;left:18px;top:80px;font-family:"Days One",sans-serif;font-size:21px;line-height:25.5px;color:var(--hero-blue);letter-spacing:.5px}
.services{position:absolute;left:116px;top:414px;width:697px;height:181px;background:linear-gradient(#33404e,var(--navy));border-radius:0 0 6px 6px;display:flex}
.service{width:174px;padding:14px 10px 0 15px;border-right:1px solid #25303c}
.service:last-child{border:0}
.service-head{display:flex;align-items:center;gap:6px;height:24px}
.service-head h3{font-size:12.5px;font-weight:700;color:#fff}
.service p{margin-top:8px;font-size:9.6px;line-height:14.5px;color:#c9d1d9}
.welcome{position:absolute;left:116px;top:613px;width:456px;height:196px;background:var(--panel);border-radius:4px;padding:12px 20px 0 21px}
.welcome h1{font-family:"Montserrat",sans-serif;font-weight:600;font-size:17px;color:var(--slate)}
.welcome h2{font-family:"Montserrat",sans-serif;font-weight:500;font-size:14.5px;line-height:17px;color:var(--slate);margin-top:7px}
.welcome p{font-size:10px;line-height:14.4px;color:#555e66;margin-top:9px}
.more{display:block;margin-top:2px;font-size:11px;font-weight:600;color:var(--orange);text-decoration:none}
.support{position:absolute;left:130px;top:850px;width:440px}
.support h2{font-family:"Montserrat",sans-serif;font-weight:500;font-size:15px;line-height:19px;color:var(--slate)}
.support p{margin-top:9px;font-size:10px;line-height:14px;color:var(--muted)}
.col-divider{position:absolute;left:601px;top:600px;width:2px;height:425px;background:linear-gradient(#e6e6e6,#f4f4f4 70%,#fff)}
.testimonial{position:absolute;left:626px;top:618px;width:195px}
.testimonial h2{font-family:"Montserrat",sans-serif;font-weight:600;font-size:17px;color:var(--slate)}
.quote-icon{position:absolute;right:10px;top:0}
.quote-mark{position:absolute;left:0;top:30px;font-family:Georgia,serif;font-size:50px;line-height:50px;color:#c9cdd2}
.testimonial blockquote{margin:12px 0 0 35px;font-size:9.8px;line-height:14px;font-style:italic;color:var(--muted)}
.cite{margin:7px 0 0 37px;font-size:9.6px;line-height:11px;font-style:italic}
.cite strong{display:block;color:#1f2a35}
.cite span{color:#6c7580}
.promo{position:absolute;left:626px;top:792px;width:187px;height:186px;border-radius:4px;background:linear-gradient(90deg,#9fb1c7,#c9d6e4 45%,#eef2f6 60%,#dfe4ea);overflow:hidden}
.promo-text{position:absolute;left:93px;top:10px;width:90px;font-size:11px;line-height:14.5px;color:#1c1c1c}
.promo-text strong{font-weight:400;font-size:12.5px;line-height:14px;display:block}
.site-footer{position:absolute;left:0;top:1026px;width:931px;height:174px;background:var(--navy-footer)}
.footer-col{position:absolute;top:23px}
.footer-col h4{font-family:"Montserrat",sans-serif;font-size:9px;font-weight:700;color:#fff;letter-spacing:.3px}
.quick-links{left:116px}
.quick-links ul{list-style:none;margin-top:9px}
.quick-links li{font-size:9.6px;line-height:17.4px;color:#8996a3}
.location{left:251px}
.location p{margin-top:9px;font-size:9.2px;line-height:13px;color:#8996a3}
.location .lbl{display:inline-block;width:38px}
.subscribe{left:433px}
.email-field{margin-top:9px;width:149px;height:25px;background:#1c262e;border:1px solid #39444f;color:#cfd5db;font-size:9px;padding:5px 6px}
.signup{margin-top:9px;width:69px;height:25px;background:var(--orange-deep);color:#fff;font-size:10px;display:flex;align-items:center;justify-content:center}
.footer-brand{position:absolute;left:615px;top:24px;display:flex;gap:8px;align-items:flex-start}
.footer-brand .brand-dot{width:22px;height:22px;margin-top:1px}
.copy{font-family:"Montserrat",sans-serif;font-size:9px;font-weight:700;line-height:13px;color:#fff}
.copy span{display:block;color:#5f6c78}
.social{position:absolute;left:655px;top:115px;display:flex;align-items:center;gap:6px}
.social-label{font-size:9px;color:#5f6c78;margin-right:6px;letter-spacing:.3px}
.social-box{width:23px;height:23px;border-radius:3px;background:#b9c3cc}
</style>
</head>
<body>
<div class="top-band"></div>
<div class="fade-band"></div>

<header>
  <div class="brand"><span class="brand-name">VANTRY FORGE</span><span class="brand-dot"></span></div>
  <div class="header-contact">
    <div class="phone">+1 615 555 0142</div>
    <div class="email">info@vfllc.example</div>
  </div>
  <nav class="main-nav">
    <a href="#" style="width:98px">HOME</a>
    <a href="#" style="width:103px">ABOUT</a>
    <a href="#" style="width:124px">SERVICES</a>
    <a href="#" style="width:151px">TESTIMONIALS</a>
    <a href="#" style="width:97px">NEWS</a>
    <a href="#" style="width:124px">CONTACT</a>
  </nav>
</header>

<section class="hero" role="img" aria-label="Photo of a smiling support agent wearing a headset in a bright call centre">
  <h2 class="hero-title">LOREM IPSUM<br>DOLOR SIT AMET,<br>CONSECTETUR<br>ADIPISICING ELIT</h2>
</section>

<section class="services">
  <div class="service">
    <div class="service-head">
      <svg width="22" height="22" viewBox="0 0 22 22"><rect x="1" y="4" width="15" height="15" rx="2" fill="none" stroke="#f39417" stroke-width="2.5"/><path d="M8 14l1-4 9-9 3 3-9 9z" fill="#f39417"/></svg>
      <h3>Network Design</h3>
    </div>
    <p>Lorem ipsum dolor sit amet, consectetur adipisicing elit, sed do eiusmod tempor incididunt ut labore et dolore magna aliqua. Ut enim ad minim veniam, quis nostrud exercitation ullamco laboris nisi ut aliquip ex ea commodo consequat.</p>
  </div>
  <div class="service">
    <div class="service-head">
      <svg width="24" height="24" viewBox="0 0 24 24"><circle cx="12" cy="13" r="8.5" fill="none" stroke="#f39417" stroke-width="2.5"/><path d="M12 8v5l3 2" stroke="#f39417" stroke-width="2" fill="none"/><circle cx="4" cy="4" r="2.5" fill="#f39417"/><circle cx="20" cy="4" r="2.5" fill="#f39417"/></svg>
      <h3>Managed Services</h3>
    </div>
    <p>Lorem ipsum dolor sit amet, consectetur adipisicing elit, sed do eiusmod tempor incididunt ut labore et dolore magna aliqua. Ut enim ad minim veniam, quis nostrud exercitation ullamco laboris nisi ut aliquip ex ea commodo consequat.</p>
  </div>
  <div class="service">
    <div class="service-head">
      <svg width="22" height="24" viewBox="0 0 22 24"><path d="M5 11V7a6 6 0 0 1 12 0v4" fill="none" stroke="#f39417" stroke-width="2.5"/><rect x="2" y="11" width="18" height="12" rx="2" fill="#f39417"/><circle cx="11" cy="16" r="1.8" fill="#2a3644"/></svg>
      <h3>Network Security</h3>
    </div>
    <p>Lorem ipsum dolor sit amet, consectetur adipisicing elit, sed do eiusmod tempor incididunt ut labore et dolore magna aliqua. Ut enim ad minim veniam, quis nostrud exercitation ullamco laboris nisi ut aliquip ex ea commodo consequat.</p>
  </div>
  <div class="service">
    <div class="service-head">
      <svg width="26" height="22" viewBox="0 0 26 22"><path d="M1 8l6-5 5 3 5-3 8 5-9 10z" fill="none" stroke="#f39417" stroke-width="2" stroke-linejoin="round"/><path d="M8 12l4 4M10 10l4 4M12 8l4 4" stroke="#f39417" stroke-width="1.6"/></svg>
      <h3>Project Management</h3>
    </div>
    <p>Lorem ipsum dolor sit amet, consectetur adipisicing elit, sed do eiusmod tempor incididunt ut labore et dolore magna aliqua. Ut enim ad minim veniam, quis nostrud exercitation ullamco laboris nisi ut aliquip ex ea commodo consequat.</p>
  </div>
</section>

<main>
  <article class="welcome">
    <h1>Welcome to Vantry Forge</h1>
    <h2>Lorem ipsum dolor sit amet, consectetur adipisicing elit</h2>
    <p>Lorem ipsum dolor sit amet, consectetur adipisicing elit, sed do eiusmod tempor incididunt ut labore et dolore magna aliqua. Ut enim ad minim veniam, quis nostrud exercitation ullamco laboris nisi ut aliquip ex ea commodo consequat. Duis aute irure dolor in reprehenderit in voluptate velit esse cillum dolore eu fugiat nulla pariatur. Excepteur sint occaecat cupidatat non proident, sunt in culpa qui officia deserunt mollit anim id est laborum.</p>
    <a class="more" href="#">+more</a>
  </article>

  <article class="support">
    <h2>Comprehensive computer network support for your business</h2>
    <p>Vantry Forge provides comprehensive computer network support to businesses that are ready to stop trying to fix technology and are ready to get back to work. Our qualified engineers will partner with you and your business to ensure you are taking advantage of all technical resources available to you – allowing you to focus on your business versus the technology that keeps it running.</p>
  </article>
</main>

<div class="col-divider"></div>

<aside class="testimonial">
  <h2>Testimonial</h2>
  <svg class="quote-icon" width="24" height="22" viewBox="0 0 24 22"><rect x="9" y="0" width="15" height="11" rx="3" fill="#f39417"/><circle cx="7" cy="11" r="4" fill="#f39417"/><path d="M0 22a7 7 0 0 1 14 0z" fill="#f39417"/></svg>
  <div class="quote-mark">&ldquo;</div>
  <blockquote>Lorem ipsum dolor sit amet, consectetur adipisicing elit, sed do eiusmod tempor incididunt ut labore et dolore magna aliqua. Ut enim ad minim veniam, quis nostrud...</blockquote>
  <p class="cite"><strong>Dana Whitcombe, IT Director</strong><span>Larkpoint Credit Union</span></p>
</aside>

<aside class="promo" role="img" aria-label="Photo of a businessman in shirt and tie working at a desktop computer">
  <p class="promo-text"><strong>Anytime –<br>Any Business</strong>will need an IT guy to Handle IT needs!!!"</p>
</aside>

<footer class="site-footer">
  <div class="footer-col quick-links">
    <h4>QUICK LINKS</h4>
    <ul><li>Home</li><li>About</li><li>Services</li><li>Testimonials</li><li>News</li><li>Contact</li></ul>
  </div>
  <div class="footer-col location">
    <h4>LOCATION</h4>
    <p>517 Calder Ln W, Nashville, TN 37288<br>
    <span class="lbl">Phone:</span>615.555.0187<br>
    <span class="lbl">Fax:</span>615.555.0187<br>
    <span class="lbl">Email:</span>info@vfllc.example</p>
  </div>
  <div class="footer-col subscribe">
    <h4>SUBSCRIBE TO UPDATES</h4>
    <div class="email-field">Enter your email address</div>
    <div class="signup">+ Sign Up</div>
  </div>
  <div class="footer-brand">
    <span class="brand-dot"></span>
    <p class="copy">© COPYRIGHT 2012 VANTRY FORGE.<span>ALL RIGHTS RESERVED.</span></p>
  </div>
  <div class="social">
    <span class="social-label">FIND US ON THEWEB</span>
    <span class="social-box"></span>
    <span class="social-box"></span>
  </div>
</footer>
</body>
</html>
```